Business card for a vending machine business

I need a business card for my vending machine business. The name is Brightwell Snacks, LLC. The card is one-sided, and landscape format. Not portrait.

The information for the card is as follows:

Dora Quinlan
Owner
(555) 314-2096
Brightwellsnacks.example
Info@brightwellsnacks.example

I'd like colors and design elements to match what's in my logo and company name. I'd like to have the checkered flag or racing stripe if possible You can use a border if youd like. You can use a background color if it looks nice and doesn't clash with the logo
Use your creativity. But a white background is perfectly fine. The card can be as simple, yet gets the point across to match the company name and logo.

I uploaded a copy of my logo. I also uploaded a businesses card I started to create, but since it was missing something, I gave up. Another upload has a red thunderbolt and the checkerer flag. Those two uploads are for inspiration. Again, please make sure to make the card landscape, not portrait. Thank you, designers. Good luck to all.

```html
<!DOCTYPE html>
<html lang="en">
<head>
<meta charset="utf-8">
<title>Brightwell Snacks – Business Card</title>
<link href="https://fonts.googleapis.com/css2?family=Audiowide&family=Arimo:wght@400;700&display=swap" rel="stylesheet">
<style>
  :root {
    --page: #2b2b2b;
    --card-light: #ffffff;
    --card-shade: #e4e4e4;
    --band: #141414;
    --red: #e3262c;
    --ink: #111111;
    --muted: #555555;
  }
  * { box-sizing: border-box; margin: 0; padding: 0; }
  html, body {
    width: 1200px; height: 900px; overflow: hidden;
    background: var(--page);
  }
  .canvas {
    width: 1200px; height: 900px;
    display: flex; align-items: center; justify-content: center;
  }
  .card {
    position: relative;
    width: 980px; height: 560px;
    border-radius: 8px 80px 8px 80px;
    background: linear-gradient(200deg, var(--card-light) 0%, #f2f2f2 45%, var(--card-shade) 100%);
    box-shadow: 0 20px 50px rgba(0,0,0,.5);
    overflow: hidden;
    font-family: "Arimo", Arial, sans-serif;
  }
  .name-band {
    position: absolute; left: 0; top: 150px;
    width: 420px; height: 56px;
    background: var(--band);
    display: flex; align-items: center;
    padding-left: 70px;
  }
  .name {
    font-family: "Audiowide", sans-serif;
    color: var(--red);
    font-size: 32px; letter-spacing: 1px;
    text-transform: uppercase;
  }
  .flag-fade {
    position: absolute; left: 420px; top: 136px;
  }
  .role {
    position: absolute; left: 90px; top: 216px;
    font-size: 24px; color: var(--muted);
  }
  .contacts {
    position: absolute; left: 130px; top: 272px;
    list-style: none;
  }
  .contacts li {
    display: flex; align-items: center; gap: 14px;
    font-size: 25px; color: #333;
    height: 40px;
  }
  .contacts svg { width: 24px; height: 24px; flex: none; }
  .divider {
    position: absolute; left: 130px; top: 418px;
    width: 420px; height: 2px; background: var(--red);
  }
  .tagline {
    position: absolute; left: 130px; top: 432px;
    font-size: 28px; font-weight: 700; color: var(--ink);
  }
  .brand {
    position: absolute; left: 640px; top: 200px;
    width: 300px;
    display: flex; flex-direction: column; align-items: center; gap: 18px;
  }
  .brand-mark {
    width: 40px; height: 40px; background: var(--red);
  }
  .brand-name {
    font-family: "Audiowide", sans-serif;
    color: var(--red);
    font-size: 40px; line-height: 1.15;
    text-align: center; text-transform: uppercase;
  }
</style>
</head>
<body>
<div class="canvas">
  <article class="card">
    <div class="name-band"><span class="name">Dora Quinlan</span></div>
    <svg class="flag-fade" width="110" height="70" role="img" aria-label="Checkered flag accent fading out">
      <defs>
        <linearGradient id="fade" x1="0" x2="1">
          <stop offset="0" stop-color="#141414"/>
          <stop offset="1" stop-color="#141414" stop-opacity="0"/>
        </linearGradient>
      </defs>
      <rect x="0" y="14" width="110" height="56" fill="url(#fade)"/>
    </svg>
    <p class="role">Owner</p>
    <ul class="contacts">
      <li>
        <svg viewBox="0 0 24 24"><path fill="#111" d="M6.6 10.8a15 15 0 0 0 6.6 6.6l2.2-2.2c.3-.3.7-.4 1-.2 1.1.4 2.3.6 3.6.6.6 0 1 .4 1 1V20c0 .6-.4 1-1 1A17 17 0 0 1 3 4c0-.6.4-1 1-1h3.5c.6 0 1 .4 1 1 0 1.3.2 2.5.6 3.6.1.3 0 .7-.2 1z"/></svg>
        (555) 314-2096
      </li>
      <li>
        <svg viewBox="0 0 24 24"><rect x="2" y="5" width="20" height="14" fill="#111"/><path d="M2 5l10 8 10-8" fill="none" stroke="#fff" stroke-width="1.6"/></svg>
        Info@brightwellsnacks.example
      </li>
      <li>
        <svg viewBox="0 0 24 24" fill="none" stroke="#111" stroke-width="1.6"><circle cx="12" cy="12" r="10"/><ellipse cx="12" cy="12" rx="4.5" ry="10"/><path d="M2 12h20M4 7h16M4 17h16"/></svg>
        Brightwellsnacks.example
      </li>
    </ul>
    <div class="divider"></div>
    <p class="tagline">We Fuel Your Day With Snacks</p>
    <div class="brand">
      <span class="brand-mark"></span>
      <span class="brand-name">Brightwell<br>Snacks</span>
    </div>
  </article>
</div>
</body>
</html>
```